Community Management Cooperative Needs a Postcard Design

This will be the first postcard in a 3 part series to be sent to 2,500 management companies in the United States. Neighborhood & Residents Purchasing Alliance helps management companies and communities save money by combining their buying power to drive down costs on everyday business needs. Their membership in the cooperative also connects with other like minded companies in the industry allowing them to share ideas and best practices with one another so that they may improve their business practices. Visit http://joinvelarta.com for more information about the company.

The purpose of this postcard is to get potential members to visit our website to find out more about the cooperative and hopefully apply to become a member. This postcard should convey a message along the lines of "we want you" or "joining forces". I would like to use bright colors and make it eye catching. Can be things along the lines of (but not limited to) super heroes coming together or a patriotic theme, etc. Postcard does not have to be limited to company color palette but provided for reference.
Updates

Target Market(s)

Independent community management companies in the United States, mostly around metropolitan areas. CEO's of companies are usually male and older, 50+

Industry/Entity Type

Community

Requirements
Must have
• Must incorporate our name, logo, and website into the design with a call to action to visit the website.
• http://joinvelarta.com

```html
<!DOCTYPE html>
<html lang="en">
<head>
<meta charset="utf-8">
<title>Neighborhood &amp; Residents Purchasing Alliance – Postcard Back</title>
<link rel="stylesheet" href="https://fonts.googleapis.com/css2?family=Catamaran:wght@500;600;700&family=Open+Sans:wght@400;600&display=swap">
<style>
  :root {
    --plum: #761f56;
    --sage: #d1e3a7;
    --sage-light: #e6f0cc;
    --ink: #2b2b2b;
    --paper: #ffffff;
    --backdrop: #7b7e81;
    --rule: #8a8a8a;
  }
  * { box-sizing: border-box; margin: 0; padding: 0; }
  html, body { width: 1200px; height: 825px; overflow: hidden; }
  body { background: var(--backdrop); position: relative; font-family: "Open Sans", Arial, sans-serif; color: var(--ink); }

  .postcard { position: absolute; left: 74px; top: 75px; width: 1048px; height: 673px; background: var(--paper); }

  .services { position: absolute; left: 15px; top: 15px; width: 676px; height: 183px; background: var(--plum); }
  .pill-heading {
    position: absolute; font-family: "Catamaran", sans-serif; font-weight: 600;
    color: var(--plum); letter-spacing: 0.5px; border-radius: 22px;
    display: flex; align-items: center; justify-content: center;
  }
  .services .pill-heading { left: 34px; top: 29px; width: 266px; height: 40px; background: var(--paper); border: 3px solid var(--sage); font-size: 26px; }
  .service-list { position: absolute; top: 84px; list-style: none; }
  .service-list.col-a { left: 38px; }
  .service-list.col-b { left: 345px; }
  .service-list li {
    display: flex; align-items: center; height: 28px;
    font-family: "Catamaran", sans-serif; font-weight: 600; font-size: 21.5px; color: var(--paper);
  }
  .service-list svg { width: 20px; height: 20px; margin-right: 14px; flex: none; }

  .about { position: absolute; left: 15px; top: 197px; width: 489px; height: 388px; background: var(--sage); }
  .about .pill-heading { left: 29px; top: 18px; width: 216px; height: 39px; border: 3px solid var(--plum); font-size: 26px; }
  .about-copy { position: absolute; left: 32px; top: 71px; width: 432px; font-size: 13.6px; line-height: 18px; color: #262626; }
  .about-copy p + p { margin-top: 18px; }
  .cta { position: absolute; left: 32px; top: 336px; display: flex; align-items: center; }
  .cta-label { font-family: "Catamaran", sans-serif; font-weight: 500; font-size: 21px; color: var(--plum); margin-right: 14px; letter-spacing: 0.3px; }
  .cta-url {
    display: flex; align-items: center; justify-content: center; width: 290px; height: 42px;
    background: var(--plum); border: 3px solid var(--paper); border-radius: 22px;
    font-family: "Catamaran", sans-serif; font-weight: 500; font-size: 21px; color: var(--paper); letter-spacing: 0.5px;
  }
  .cta-url strong { font-weight: 700; }

  .sender { position: absolute; left: 704px; top: 31px; width: 200px; }
  .brand { display: flex; align-items: center; margin-bottom: 8px; }
  .brand-mark { width: 20px; height: 20px; background: var(--plum); flex: none; margin-right: 8px; }
  .brand-name { font-family: "Catamaran", sans-serif; font-weight: 700; font-size: 11px; line-height: 11px; color: var(--plum); letter-spacing: 0.8px; text-transform: uppercase; }
  .sender address { font-style: normal; font-size: 12px; line-height: 13px; color: var(--ink); }
  .sender .phone { font-size: 17px; margin-top: 10px; line-height: 18px; }
  .sender .email { font-size: 11.5px; line-height: 13px; }

  .stamp-box { position: absolute; left: 929px; top: 33px; width: 89px; height: 99px; border: 1px solid #333; }
  .address-line { position: absolute; left: 688px; width: 274px; height: 1px; background: var(--rule); }
</style>
</head>
<body>
  <main class="postcard">
    <section class="services">
      <h2 class="pill-heading">SERVICES FOR YOU</h2>
      <ul class="service-list col-a">
        <li><svg viewBox="0 0 20 20"><circle cx="10" cy="10" r="8.5" fill="var(--sage-light)" stroke="#fff" stroke-width="2"/><path d="M5.8 10.2l2.8 2.8 5.6-5.8" fill="none" stroke="var(--plum)" stroke-width="2.2" stroke-linecap="round" stroke-linejoin="round"/></svg>Peer-to-Peer Networking</li>
        <li><svg viewBox="0 0 20 20"><circle cx="10" cy="10" r="8.5" fill="var(--sage-light)" stroke="#fff" stroke-width="2"/><path d="M5.8 10.2l2.8 2.8 5.6-5.8" fill="none" stroke="var(--plum)" stroke-width="2.2" stroke-linecap="round" stroke-linejoin="round"/></svg>Marketing Toolkit</li>
        <li><svg viewBox="0 0 20 20"><circle cx="10" cy="10" r="8.5" fill="var(--sage-light)" stroke="#fff" stroke-width="2"/><path d="M5.8 10.2l2.8 2.8 5.6-5.8" fill="none" stroke="var(--plum)" stroke-width="2.2" stroke-linecap="round" stroke-linejoin="round"/></svg>Social Boost</li>
      </ul>
      <ul class="service-list col-b">
        <li><svg viewBox="0 0 20 20"><circle cx="10" cy="10" r="8.5" fill="var(--sage-light)" stroke="#fff" stroke-width="2"/><path d="M5.8 10.2l2.8 2.8 5.6-5.8" fill="none" stroke="var(--plum)" stroke-width="2.2" stroke-linecap="round" stroke-linejoin="round"/></svg>Reputation Management</li>
        <li><svg viewBox="0 0 20 20"><circle cx="10" cy="10" r="8.5" fill="var(--sage-light)" stroke="#fff" stroke-width="2"/><path d="M5.8 10.2l2.8 2.8 5.6-5.8" fill="none" stroke="var(--plum)" stroke-width="2.2" stroke-linecap="round" stroke-linejoin="round"/></svg>Member Savings Consultant</li>
        <li><svg viewBox="0 0 20 20"><circle cx="10" cy="10" r="8.5" fill="var(--sage-light)" stroke="#fff" stroke-width="2"/><path d="M5.8 10.2l2.8 2.8 5.6-5.8" fill="none" stroke="var(--plum)" stroke-width="2.2" stroke-linecap="round" stroke-linejoin="round"/></svg>Secure Member Website</li>
      </ul>
    </section>

    <section class="about">
      <h2 class="pill-heading">WHO WE ARE</h2>
      <div class="about-copy">
        <p>Comprised of the most talented and progressive companies in North America, NRPA (Neighborhood &amp; Residents Purchasing Alliance) aims to help members seize opportunities and improve profitability. We are a select group of independently owned Homeowner Associations and Management Companies focused on securing our futures, increasing our competitiveness, and offering our clients an unforgettable experience.</p>
        <p>Fresh thinking, integrity, and delivering unparalleled service are at the heart of everything we do. We bring together likeminded members to leverage the power of scale. Our services are centered on empowering you to improve your bottom line through purchasing power, marketing, and the ability to offer your clients and members more.</p>
      </div>
      <div class="cta">
        <span class="cta-label">JOIN US NOW</span>
        <span class="cta-url">WWW.<strong>JOINVELARTA</strong>.COM</span>
      </div>
    </section>

    <aside class="sender">
      <div class="brand">
        <span class="brand-mark"></span>
        <span class="brand-name">Neighborhood &amp; Residents<br>Purchasing Alliance</span>
      </div>
      <address>
        418 Linden Harbor Road<br>Concord, NH 03301
        <div class="phone">P: 919.555.0142</div>
        <div class="email">E: jbarrow@velartagroup.com</div>
      </address>
    </aside>

    <div class="stamp-box"></div>
    <div class="address-line" style="top:344px"></div>
    <div class="address-line" style="top:406px"></div>
    <div class="address-line" style="top:463px"></div>
  </main>
</body>
</html>
```